Automotive Business Card Design

I would just like a automotive themed card. nothing too extravagant, but catchy.

needs to say something about doing roadside assistance,mobile repairs, Diesel repairs, and Fleet maintenance

it can be single sided or double sided. no preference there.

Industry/Entity Type

Automotive

Contact Information for Business Card

Dean Marwick
phone 519 374 2083
Name: Brightway Automotive & Diesel Repair

```html
<!DOCTYPE html>
<html lang="en">
<head>
<meta charset="utf-8">
<title>Brightway Automotive &amp; Diesel Repair – Business Card</title>
<link rel="stylesheet" href="https://fonts.googleapis.com/css2?family=Cinzel:wght@400&family=Open+Sans:wght@400&display=swap">
<style>
  :root {
    --page-bg: #2b2b2d;
    --card-bg: #ffffff;
    --ink: #111111;
    --rule: #b9b2a6;
    --photo-engine-a: #d4d5d8;
    --photo-engine-b: #8f9094;
    --photo-parts-a: #ffffff;
    --photo-parts-b: #d2d4d8;
  }
  * { box-sizing: border-box; margin: 0; padding: 0; }
  html, body {
    width: 1200px; height: 900px; overflow: hidden;
    background: var(--page-bg);
  }
  .card {
    position: absolute; left: 75px; top: 150px;
    width: 1050px; height: 600px;
    background: var(--card-bg);
    overflow: hidden;
    font-family: "Open Sans", sans-serif;
    color: var(--ink);
  }
  .photo-engine {
    position: absolute; left: 0; top: 0;
    width: 400px; height: 285px;
    background: linear-gradient(135deg, var(--photo-engine-a), var(--photo-engine-b));
  }
  .photo-parts {
    position: absolute; left: 400px; top: 0;
    width: 650px; height: 255px;
    background: linear-gradient(180deg, var(--photo-parts-a), var(--photo-parts-b) 50%, var(--photo-parts-a));
  }
  .title-rule {
    position: absolute; left: 560px; top: 268px;
    width: 450px; height: 1px; background: var(--rule);
  }
  .business-name {
    position: absolute; left: 150px; top: 290px; width: 870px;
    font-family: "Cinzel", serif; font-size: 35px; font-weight: 400;
    letter-spacing: 1px; text-align: right; white-space: nowrap;
    line-height: 1.2;
  }
  .services {
    position: absolute; left: 640px; top: 360px;
  }
  .services-heading { font-size: 25px; font-weight: 400; margin-bottom: 6px; }
  .services-list { list-style: none; padding-left: 100px; }
  .services-list li {
    position: relative; font-size: 20px; line-height: 30px; white-space: nowrap;
  }
  .services-list li::before {
    content: ""; position: absolute; left: -30px; top: 10px;
    width: 10px; height: 10px; border-radius: 50%; background: var(--ink);
  }
  .services-list li:nth-child(2) { margin-left: 20px; }
  .services-list li:nth-child(3) { margin-left: 40px; }
  .services-list li:nth-child(4) { margin-left: 60px; }
  .contact {
    position: absolute; left: 60px; top: 445px;
    border-left: 5px solid var(--ink); padding-left: 28px;
  }
  .contact-name { font-size: 38px; font-weight: 400; line-height: 52px; }
  .contact-phone {
    display: flex; align-items: center; gap: 26px;
    font-size: 21px; margin-top: 8px;
  }
  .contact-phone svg { width: 16px; height: 16px; }
</style>
</head>
<body>
  <div class="card">
    <div class="photo-engine" role="img" aria-label="Photo of motor oil being poured into an engine"></div>
    <div class="photo-parts" role="img" aria-label="Photo of assorted engine parts"></div>
    <div class="title-rule"></div>
    <h1 class="business-name">Brightway Automotive &amp; Diesel Repair</h1>

    <section class="services">
      <h2 class="services-heading">Services</h2>
      <ul class="services-list">
        <li>Roadside assistance</li>
        <li>Fleet maintenance</li>
        <li>Diesel repairs</li>
        <li>Mobile repairs</li>
      </ul>
    </section>

    <section class="contact">
      <p class="contact-name">Dean Marwick</p>
      <p class="contact-phone">
        <svg viewBox="0 0 24 24" aria-hidden="true"><path fill="#111" d="M6.6 10.8a15.1 15.1 0 0 0 6.6 6.6l2.2-2.2a1 1 0 0 1 1-.25 11.4 11.4 0 0 0 3.6.57 1 1 0 0 1 1 1V20a1 1 0 0 1-1 1A17 17 0 0 1 3 4a1 1 0 0 1 1-1h3.5a1 1 0 0 1 1 1c0 1.25.2 2.45.57 3.57a1 1 0 0 1-.25 1z"/></svg>
        <span>519 374 2083</span>
      </p>
    </section>
  </div>
</body>
</html>
```